Veltorquin.io - Please redesign to make it look better from current design

We already have the current website, that you can access but we think it can improve from current version.
Veltorquin is a cryptocurrency hedge fund that allow you to participate in the hedge fund with cryptocurrency such as eth.
At current phase, we are doing an ICO, then we want to make sure that the website it looks professional, beautiful and trustable enough for investors after looking at our website.
Target Market(s)
Investors
Industry/Entity Type
Investment
Coding
Coded - Design and coding required
Number of Pages Required
1 page
Look and feel

```html
<!DOCTYPE html>
<html lang="en">
<head>
<meta charset="utf-8">
<title>Veltorquin.io – Digital Asset Management</title>
<link href="https://fonts.googleapis.com/css2?family=Roboto:ital,wght@0,300;0,400;0,500;1,400&family=Open+Sans:wght@400;600;700&display=swap" rel="stylesheet">
<style>
:root{
  --navy:#13248a;
  --blue:#1a2c94;
  --sky:#c9ecfb;
  --sky-soft:#d8f2fd;
  --grey-bg:#eeeeee;
  --text:#333;
  --muted:#555;
  --line:#cfcfcf;
  --white:#fff;
}
*{box-sizing:border-box;margin:0;padding:0}
html,body{width:1200px;height:2908px;overflow:hidden}
body{font-family:"Open Sans",sans-serif;color:var(--text);background:var(--white);position:relative}
section,header,footer{position:absolute;left:0;width:1200px}
.abs{position:absolute}

/* header */
.site-header{top:0;height:110px}
.brand{left:78px;top:22px;display:flex;align-items:center;gap:12px}
.brand-dot{width:40px;height:40px;border-radius:50%;background:var(--navy)}
.brand-name{font-family:"Roboto",sans-serif;font-size:24px;font-weight:500;color:var(--navy)}
.main-nav{right:78px;top:52px;display:flex;gap:54px;font-family:"Roboto",sans-serif;font-size:17px;color:#111}

/* hero */
.hero{top:0;height:679px}
.hero-title{left:78px;top:248px;font-family:"Roboto",sans-serif;font-weight:300;font-size:84px;color:var(--navy);line-height:1}
.hero-sub{left:78px;top:358px;font-family:"Roboto",sans-serif;font-weight:300;font-size:40px;color:var(--navy)}
.hero-rule{left:78px;top:436px;width:64px;height:2px;background:var(--navy)}
.hero-text{left:78px;top:464px;width:540px;font-size:19px;line-height:25px;color:var(--muted)}
.hero-art{left:611px;top:116px;width:589px;height:563px;background:linear-gradient(135deg,#f4f6fd,#dfe5f8)}

/* about */
.about{top:679px;height:385px;background:var(--navy);color:var(--white);text-align:center}
.section-title{font-family:"Roboto",sans-serif;font-weight:300;font-size:42px;letter-spacing:.5px}
.about .section-title{margin-top:52px}
.about-text{width:800px;margin:16px auto 0;font-size:16.5px;line-height:24px}
.btn{display:inline-block;background:var(--sky);color:var(--navy);font-family:"Roboto",sans-serif;font-weight:500;font-size:16px;text-align:center}
.about .btn{margin-top:26px;width:167px;height:51px;line-height:51px}

/* team */
.team{top:1064px;height:565px;background:var(--grey-bg)}
.team .section-title{text-align:center;margin-top:48px;color:#111}
.card{top:129px;width:322px;height:384px;background:var(--white);box-shadow:0 2px 5px rgba(0,0,0,.18);padding:20px 12px}
.card-head{display:flex;align-items:center;gap:12px;height:88px}
.avatar{width:86px;height:86px;border-radius:50%;background:radial-gradient(circle at 50% 40%,#9a7a62,#4b3b33);flex:none}
.role{font-family:"Roboto",sans-serif;font-style:italic;font-size:15px;color:#222}
.name{font-family:"Roboto",sans-serif;font-size:18px;color:var(--blue);margin-top:6px}
.bio{margin-top:30px;font-size:15.5px;line-height:25px;color:var(--muted)}

/* process */
.process{top:1629px;height:415px;background:var(--navy);color:var(--white)}
.process .section-title{position:absolute;left:78px;top:44px}
.process-sub{left:78px;top:132px;font-family:"Roboto",sans-serif;font-size:29px}
.process-text{left:78px;top:184px;width:510px;font-size:16.5px;line-height:25px}
.process-art{left:679px;top:87px;width:330px;height:223px;background:linear-gradient(135deg,#2a3c9c,#1b2d8f);border-radius:4px}

/* distribution */
.distribution{top:2044px;height:508px}
.dist-title{width:100%;top:46px;text-align:center;font-family:"Roboto",sans-serif;font-size:31px;color:var(--blue)}
.dist-svg{left:0;top:0}
.dist-label{font-family:"Open Sans",sans-serif;font-size:19px;color:#222;line-height:22px}
.dist-label small{font-size:13px}
.dist-label .note{display:block;font-size:13.5px;color:#333}
.dist-center{left:0;width:1200px;top:202px;text-align:center;font-family:"Roboto",sans-serif;font-size:22px;font-weight:500;color:var(--navy)}
.remainder{width:100%;top:432px;text-align:center;font-size:17px;color:#222}

/* footer */
.site-footer{top:2552px;height:356px;background:var(--navy);color:var(--white)}
.foot-head{font-family:"Roboto",sans-serif;font-size:21px;top:42px}
.foot-text{font-size:15.5px;line-height:25px}
.site-footer .btn{width:167px;height:51px;line-height:51px}
.pin{width:20px;height:26px}
.foot-brand{font-family:"Roboto",sans-serif;font-size:22px;letter-spacing:1px}
.email{left:639px;top:168px;width:270px;height:51px;background:var(--white);color:#888;font-size:14px;padding:0 22px;line-height:51px}
.send{left:859px;top:168px;width:50px;height:51px;background:var(--sky);display:flex;align-items:center;justify-content:center}
.big-brand{left:950px;top:60px;width:170px;text-align:center}
.big-dot{width:120px;height:120px;border-radius:50%;background:var(--white);margin:0 auto 12px}
.social{left:956px;top:196px;display:flex;gap:10px}
.social span{width:42px;height:42px;border-radius:50%;border:1.5px solid var(--white)}
.foot-rule{left:78px;top:293px;width:1044px;height:1px;background:rgba(255,255,255,.3)}
.copyright{width:100%;top:313px;text-align:center;font-size:16px}
</style>
</head>
<body>

<header class="site-header">
  <div class="abs brand"><span class="brand-dot"></span><span class="brand-name">veltorquin</span></div>
  <nav class="abs main-nav"><span>Home</span><span>About</span><span>Process</span><span>Our Team</span><span>Contact</span></nav>
</header>

<section class="hero">
  <h1 class="abs hero-title">veltorquin</h1>
  <p class="abs hero-sub">Digital Asset Management</p>
  <div class="abs hero-rule"></div>
  <p class="abs hero-text">Veltorquin enable companies and investors to facilities business operation in modern digital world, including asset management on hedge fund strategy model.</p>
  <div class="abs hero-art" role="img" aria-label="Line illustration of crypto coins, a rocket, charts and wallets connected in a network"></div>
</section>

<section class="about">
  <h2 class="section-title">ABOUT US</h2>
  <p class="about-text">Veltorquin process and manages on hedge fund strategy models which invests in a diversified portfolio of blockchain tokens. Blockchain tokens are emerging which add a monetary incentive layer to p2p protocols and facilitate equity crowdfunding that anyone in the world can participate in. This means open source software developers can monetize their networks at the protocol level and users of the network are the equity owners of the network. For this conditions, returns will go to holders of the tokens.</p>
  <span class="btn">EXPLORE MORE</span>
</section>

<section class="team">
  <h2 class="section-title">EXECUTIVE TEAM</h2>
  <article class="abs card" style="left:78px">
    <div class="card-head"><div class="avatar" role="img" aria-label="Portrait photo of the director"></div><div><p class="role">Director</p><p class="name">Daren Wolmsley</p></div></div>
    <p class="bio">As a hedge fund manager. Wolmsley is the Chief Executive Officer of Harrowgate Capital LLC, an investment manager of Corvane Metal Fund SP (Long-Short Equity Fund, investing in U.S. Stock Market) and Kestral Prime Fund (Managed Futures Fund, focusing in Japanese Futures Market) Both based in Tokyo.</p>
  </article>
  <article class="abs card" style="left:440px">
    <div class="card-head"><div class="avatar" role="img" aria-label="Portrait photo of the technical advisor" style="background:radial-gradient(circle at 50% 40%,#b9a78f,#5a6a4f)"></div><div><p class="role">Technical advisor</p><p class="name">Kesh Tarrovan</p></div></div>
    <p class="bio">Tarrovan has various experienced on cryptocurrency and blockchain technology. He created what was the world's 4th most valuable cryptocurrency in February 2014. He is also the world's first person to implement stealth addresses in NV-Wallets, improving cryptocurrency anonymity.</p>
  </article>
  <article class="abs card" style="left:801px">
    <div class="card-head"><div class="avatar" role="img" aria-label="Portrait photo of the marketing consultant" style="background:radial-gradient(circle at 50% 40%,#a57452,#6b2a1e)"></div><div><p class="role">Marketing Consultant</p><p class="name">Orin Vasquell</p></div></div>
    <p class="bio">Vasquell embeds a decade of experience in brand building, strategic planning, and marketing communication across the global agencies, such as Brightwell Group, Norlane, Halden Burke, Tessaro. His seasoned specialty focuses on exploring a new market insight to formulate disruptive strategies</p>
  </article>
</section>

<section class="process">
  <h2 class="section-title">PROCESS</h2>
  <h3 class="abs process-sub">Hedge Fund Model</h3>
  <p class="abs process-text">Veltorquin run on closed-end fund (CEF) model which offers its shares to investors and utilize the fund to speculate and invest in the innovative blockchain tokens. Veltorquin will charge an upfront annual operation fee 4% of the money raised during the ICO. After that, the fund will charge a quarterly performance of 50% on the net profit made.</p>
  <div class="abs process-art" role="img" aria-label="Icon illustration of gears beside a growth chart board"></div>
</section>

<section class="distribution">
  <h2 class="abs dist-title">Net Profit Distribution</h2>
  <svg class="abs dist-svg" width="1200" height="508" viewBox="0 0 1200 508" aria-hidden="true">
    <g stroke="#cfcfcf" stroke-width="1.5" fill="none">
      <line x1="462" y1="159" x2="737" y2="159"/>
      <line x1="194" y1="226" x2="456" y2="226"/><line x1="456" y1="226" x2="510" y2="258"/>
      <line x1="737" y1="226" x2="1008" y2="226"/><line x1="737" y1="226" x2="688" y2="258"/>
      <line x1="230" y1="391" x2="475" y2="391"/><line x1="475" y1="391" x2="549" y2="361"/>
      <line x1="720" y1="391" x2="985" y2="391"/><line x1="720" y1="391" x2="650" y2="361"/>
      <line x1="600" y1="159" x2="600" y2="186"/>
    </g>
    <polygon points="600,186 688,258 650,361 549,361 510,258" fill="#cdeffd"/>
    <g fill="#13248a">
      <circle cx="600" cy="186" r="4"/><circle cx="688" cy="258" r="4"/><circle cx="650" cy="361" r="4"/><circle cx="549" cy="361" r="4"/><circle cx="510" cy="258" r="4"/>
    </g>
  </svg>
  <p class="abs dist-center">veltorquin</p>
  <p class="abs dist-label" style="left:0;width:1200px;top:102px;text-align:center">50 %<span class="note">of net profit is distributed to investors</span></p>
  <p class="abs dist-label" style="left:213px;top:160px">0 – 5 % <small>net profit</small> &gt; 0%<span class="note">performance fee</span></p>
  <p class="abs dist-label" style="left:783px;top:160px">&gt; 15% <small>net profit</small> &gt; 15%<span class="note">performance fee</span></p>
  <p class="abs dist-label" style="left:252px;top:326px">5 – 10% <small>net profit</small> &gt; 5%<span class="note">performance fee</span></p>
  <p class="abs dist-label" style="left:745px;top:326px">10-15 % <small>net profit</small> &gt; 13%<span class="note">performance fee</span></p>
  <p class="abs remainder">The remainder (50% minus performance fee, so at least 35%) is reinvested</p>
</section>

<footer class="site-footer">
  <h4 class="abs foot-head" style="left:78px">FOR MORE INFO</h4>
  <p class="abs foot-text" style="left:78px;top:86px;width:240px">Lorem Ipsum is simply dummy text of the printing and typesetting industry. Lorem Ipsum has been the industry's.</p>
  <span class="abs btn" style="left:78px;top:198px">DOWNLOAD PDF</span>

  <h4 class="abs foot-head" style="left:355px">CONTACT INFO</h4>
  <svg class="abs pin" style="left:353px;top:84px" viewBox="0 0 20 26" aria-hidden="true"><path d="M10 0C4.5 0 0 4.4 0 9.8 0 17 10 26 10 26s10-9 10-16.2C20 4.4 15.5 0 10 0zm0 13.5a3.8 3.8 0 1 1 0-7.6 3.8 3.8 0 0 1 0 7.6z" fill="#fff"/></svg>
  <p class="abs foot-brand" style="left:384px;top:84px">veltorquin</p>
  <p class="abs foot-text" style="left:386px;top:124px;width:250px">Suite 08-12, 9/F., East Wing, Meridian Trade Centre, Portside Quay, 42, Linden Road, Westhaven, Harbor District.</p>

  <h4 class="abs foot-head" style="left:639px">NEWSLETTER</h4>
  <p class="abs foot-text" style="left:639px;top:86px;width:270px">Subscribe to Our Newsletter to get latest News &amp; Updates About Company</p>
  <div class="abs email">Enter Your E-Mail</div>
  <div class="abs send"><svg width="22" height="22" viewBox="0 0 24 24" aria-hidden="true"><path d="M2 11l20-9-7 20-3-8z" fill="none" stroke="#13248a" stroke-width="2" stroke-linejoin="round"/><path d="M12 14l10-12" stroke="#13248a" stroke-width="2"/></svg></div>

  <div class="abs big-brand"><div class="big-dot"></div><p class="foot-brand" style="font-size:16px">veltorquin</p></div>
  <div class="abs social" aria-label="Social links"><span></span><span></span><span></span></div>

  <div class="abs foot-rule"></div>
  <p class="abs copyright">© <strong>veltorquin</strong> - 2017. All Rights Reserved.</p>
</footer>

</body>
</html>
```